Create for us a Shop-Stopper Business Card

We need a standout, first class business card to go along with our new brand strategy. Sleek, Contemporary and fresh.

Colors and theme must sync with our websitewww.pelvorpower.co.uk

We want a business card that has a global brand appeal. TKR Energy is a small UK renewable company that specialises in energy projects in Africa. We want a business card that has the following characteristics: Very short, precise, global, stand out, NOT TOO LOUD but contemporary. The company's colour themes are White, Grey with a hint of green.

Target Market(s)

Business exec, high net worth individuals, investors, commercial leaders, suppliers, government officials

Industry/Entity Type

Solar Energy

Contact Information for Business Card

Logo, Name, Title, Address, web address, email,

Requirements
Must have
• Logo must be sharp
Nice to have
• Adapt fonts from the logo. The large circular side of the logo at the back in a very refreshing way
Should not have
• No solar panel shapes or image.Very little black. If possible avoid black. Its not coming out nice. I think !!!

```html
<!DOCTYPE html>
<html lang="en">
<head>
<meta charset="utf-8">
<title>TKR Energy – Business Card</title>
<link rel="stylesheet" href="https://fonts.googleapis.com/css2?family=Montserrat:wght@400;500;700&family=Roboto:wght@400&display=swap">
<style>
  :root {
    --green: #079a46;
    --green-light: #0aad55;
    --white: #ffffff;
    --card-white: #f7f7f7;
    --grey-text: #6e6e6e;
    --accent-red: #d2232a;
    --page: #ececec;
  }
  * { margin: 0; padding: 0; box-sizing: border-box; }
  html, body { width: 1200px; height: 1023px; overflow: hidden; background: var(--page); }
  .canvas { position: relative; width: 1200px; height: 1023px; }
  .card {
    position: absolute; left: 280px; width: 640px; height: 376px;
    border-radius: 18px; overflow: hidden;
    background: linear-gradient(135deg, var(--white), var(--card-white));
    box-shadow: 0 6px 18px rgba(0,0,0,0.18);
  }
  .card--front { top: 90px; }
  .card--back { top: 540px; }
  .card-shapes { position: absolute; inset: 0; }
  .brand { position: absolute; display: flex; align-items: center; gap: 12px; }
  .brand-dot { width: 34px; height: 34px; border-radius: 50%; background: var(--green); }
  .brand-name {
    font-family: "Montserrat", sans-serif; font-weight: 500;
    font-size: 34px; letter-spacing: 1px; color: var(--grey-text); line-height: 1;
  }
  .brand-rule { position: absolute; height: 1.5px; background: var(--accent-red); }
  .card--front .brand { left: 38px; top: 42px; }
  .card--front .brand-rule { left: 84px; top: 88px; width: 240px; }
  .card--back .brand { left: 38px; top: 214px; }
  .card--back .brand-rule { left: 84px; top: 260px; width: 240px; }
  .contact {
    position: absolute; right: 24px; top: 132px; list-style: none;
    font-family: "Roboto", sans-serif; font-size: 13px; color: var(--white);
    text-align: right;
  }
  .contact li { display: flex; align-items: center; justify-content: flex-end; gap: 8px; height: 22px; white-space: nowrap; }
  .contact svg { width: 13px; height: 13px; flex: none; }
  .person { position: absolute; left: 62px; top: 292px; color: var(--white); }
  .person-name { font-family: "Montserrat", sans-serif; font-weight: 700; font-size: 26px; letter-spacing: 0.5px; line-height: 1.2; }
  .person-title { font-family: "Montserrat", sans-serif; font-weight: 400; font-size: 13px; margin-left: 30px; }
</style>
</head>
<body>
<main class="canvas">

  <section class="card card--front" aria-label="Business card front">
    <svg class="card-shapes" viewBox="0 0 640 376" aria-hidden="true">
      <defs>
        <linearGradient id="greenFront" x1="0" y1="1" x2="1" y2="0">
          <stop offset="0" stop-color="#079a46"/>
          <stop offset="1" stop-color="#0aad55"/>
        </linearGradient>
      </defs>
      <path d="M0 250 H300 V112 H640 V376 H0 Z" fill="url(#greenFront)"/>
      <circle cx="300" cy="200" r="72" fill="#ffffff"/>
    </svg>
    <div class="brand">
      <span class="brand-dot"></span>
      <span class="brand-name">TKR ENERGY</span>
    </div>
    <div class="brand-rule"></div>
    <ul class="contact">
      <li>info@pelvorpower.co.uk
        <svg viewBox="0 0 14 14"><rect x="1" y="3" width="12" height="8" fill="none" stroke="#fff" stroke-width="1.2"/><path d="M1 3 L7 8 L13 3" fill="none" stroke="#fff" stroke-width="1.2"/></svg>
      </li>
      <li>www.pelvorpower.co.uk
        <svg viewBox="0 0 14 14"><circle cx="7" cy="7" r="5.5" fill="none" stroke="#fff" stroke-width="1.2"/><ellipse cx="7" cy="7" rx="2.4" ry="5.5" fill="none" stroke="#fff" stroke-width="1"/><path d="M1.5 7 H12.5" stroke="#fff" stroke-width="1"/></svg>
      </li>
      <li>N7 4QR London, United Kingdom
        <svg viewBox="0 0 14 14"><path d="M7 13 C3 8 3 6 3 5.5 A4 4 0 0 1 11 5.5 C11 6 11 8 7 13 Z" fill="#fff"/><circle cx="7" cy="5.5" r="1.5" fill="#079a46"/></svg>
      </li>
    </ul>
    <div class="person">
      <p class="person-name">Your Name</p>
      <p class="person-title">Title</p>
    </div>
  </section>

  <section class="card card--back" aria-label="Business card back">
    <svg class="card-shapes" viewBox="0 0 640 376" aria-hidden="true">
      <defs>
        <linearGradient id="greenBack" x1="0" y1="1" x2="1" y2="0">
          <stop offset="0" stop-color="#079a46"/>
          <stop offset="1" stop-color="#0aad55"/>
        </linearGradient>
      </defs>
      <path d="M0 0 H640 V300 H420 V150 H0 Z" fill="url(#greenBack)"/>
      <circle cx="420" cy="200" r="80" fill="#ffffff"/>
    </svg>
    <div class="brand">
      <span class="brand-dot"></span>
      <span class="brand-name">TKR ENERGY</span>
    </div>
    <div class="brand-rule"></div>
  </section>

</main>
</body>
</html>
```